Velmora Asset Management needs a cover page for presentations

I have a logo but would like help designing the front pages of a power point presentation. I would like an elegant front cover for all documents.

Velmora is a finance company. Velmora meals triangle. Triangle is the simplest of all polygons which make up other polygons. The front cover should look mathematical / formal and yet elegant.

I have attached the logo.
I have also attached some sample front covers fro other companies to give you an idea.

I look forward to receiving your ideas.

Target Market(s)

Financial market, investors

Contact Information for Business Card

I have added a file below with the details / information that needs to eb shown on the business card. Address / name etc... The business class should show the logo

Colors
0255a3

Requirements
Must have
• the logo

```html
<!DOCTYPE html>
<html lang="en">
<head>
<meta charset="utf-8">
<title>Velmora Asset Management – Presentation Covers</title>
<link rel="stylesheet" href="https://fonts.googleapis.com/css2?family=Cinzel:wght@400;500&family=Open+Sans:wght@400;600&display=swap">
<style>
  :root {
    --navy: #262d70;
    --navy-deep: #1d2360;
    --navy-soft: #3a4289;
    --steel: #9aa3ad;
    --mist: #eef0f3;
    --paper: #ffffff;
    --ink-muted: #5b6070;
    --rule: #8b90b0;
  }
  * { box-sizing: border-box; margin: 0; padding: 0; }
  html, body { width: 1200px; height: 3000px; overflow: hidden; background: var(--paper); }
  body { position: relative; font-family: "Open Sans", Arial, sans-serif; }

  .slide {
    position: absolute; left: 178px; width: 844px; height: 472px;
    overflow: hidden; box-shadow: 0 4px 10px rgba(0,0,0,.35);
  }
  .slide--1 { top: 14px; }
  .slide--2 { top: 514px; }
  .slide--3 { top: 1014px; }
  .slide--4 { top: 1514px; }
  .slide--5 { top: 2014px; }
  .slide--6 { top: 2514px; }

  .light { background: linear-gradient(135deg, var(--paper) 0%, var(--mist) 100%); color: var(--navy); }
  .dark { background: var(--navy); color: var(--paper); }

  .fill { position: absolute; }

  .brand { position: absolute; display: flex; align-items: center; gap: 12px; }
  .brand__mark { width: 30px; height: 30px; background: currentColor; opacity: .9; }
  .brand__name {
    font-family: "Cinzel", Georgia, serif; font-weight: 500; font-size: 19px;
    line-height: 1.1; letter-spacing: .04em; text-transform: uppercase;
  }
  .brand--right { right: 42px; }
  .brand--left { left: 48px; }

  .title {
    position: absolute; font-family: "Cinzel", Georgia, serif; font-weight: 400;
    font-size: 36px; letter-spacing: .01em; white-space: nowrap; line-height: 1;
  }
  .subtitle {
    position: absolute; font-size: 11px; font-weight: 600; letter-spacing: .02em;
    text-transform: uppercase; white-space: nowrap;
  }
  .align-right { right: 22px; text-align: right; }
  .align-left { left: 46px; }

  .site { position: absolute; font-size: 11px; white-space: nowrap; }
  .rule { position: absolute; height: 1px; background: var(--rule); }
  .dark .rule { background: rgba(255,255,255,.55); }

  /* Slide 5 */
  .divider-title {
    position: absolute; right: 34px; top: 236px; text-align: right;
    font-family: "Cinzel", Georgia, serif; font-size: 40px; line-height: 1.15;
  }
  .divider-sub { right: 34px; top: 334px; }

  /* Slide 6 */
  .banner-band { position: absolute; left: 0; top: 266px; width: 100%; height: 16px; background: #a9adb8; }
  .banner-title {
    position: absolute; left: 38px; top: 392px; font-family: "Cinzel", Georgia, serif;
    font-size: 38px; color: var(--navy); white-space: nowrap;
  }
</style>
</head>
<body>

<!-- Cover 1 : light -->
<section class="slide slide--1 light">
  <div class="fill" role="img" aria-label="Soft financial chart and world map backdrop"
       style="inset:0;background:linear-gradient(120deg,rgba(190,198,214,.25),rgba(230,233,238,.2) 60%,rgba(200,206,218,.35))"></div>
  <div class="fill" role="img" aria-label="Abstract blue geometric decoration with city photograph"
       style="left:0;top:0;width:380px;height:472px;clip-path:polygon(0 0,55% 0,100% 100%,0 100%);background:linear-gradient(160deg,#d9dde6 0%,#5a6499 45%,var(--navy) 100%);opacity:.85"></div>
  <div class="brand brand--right" style="top:44px;color:var(--navy)">
    <span class="brand__mark"></span>
    <span class="brand__name">Velmora<br>Asset Management</span>
  </div>
  <h1 class="title align-right" style="top:226px;color:var(--navy)">Your Title Goes Here</h1>
  <p class="subtitle align-right" style="top:270px;color:var(--ink-muted)">Your subtitle goes here</p>
  <span class="site" style="left:322px;top:417px;color:var(--navy)">www.velmoraam.com</span>
  <span class="rule" style="left:474px;right:22px;top:424px"></span>
</section>

<!-- Cover 2 : dark -->
<section class="slide slide--2 dark">
  <div class="fill" role="img" aria-label="Businessman overlooking city skyline with financial chart overlay"
       style="inset:0;background:linear-gradient(100deg,#3b5aa8 0%,#2e3c8a 35%,var(--navy) 60%,#2a3176 100%)"></div>
  <div class="fill" role="img" aria-label="Abstract geometric decoration"
       style="left:0;top:0;width:380px;height:472px;clip-path:polygon(0 0,55% 0,100% 100%,0 100%);background:linear-gradient(170deg,rgba(120,160,220,.35),rgba(29,35,96,.3))"></div>
  <div class="brand brand--right" style="top:54px">
    <span class="brand__mark"></span>
    <span class="brand__name">Velmora<br>Asset Management</span>
  </div>
  <h1 class="title align-right" style="top:218px">Your Title Goes Here</h1>
  <p class="subtitle align-right" style="top:262px">Your subtitle goes here</p>
  <span class="site" style="left:322px;top:417px">www.velmoraam.com</span>
  <span class="rule" style="left:474px;right:22px;top:424px"></span>
</section>

<!-- Cover 3 : light, left aligned -->
<section class="slide slide--3 light">
  <div class="fill" role="img" aria-label="Faint architectural line backdrop"
       style="inset:0;background:linear-gradient(150deg,rgba(255,255,255,0) 40%,rgba(210,214,222,.45) 100%)"></div>
  <div class="fill" role="img" aria-label="Abstract steel and navy geometric decoration"
       style="right:0;top:0;width:330px;height:472px;clip-path:polygon(100% 0,100% 100%,0 100%,40% 60%);background:linear-gradient(200deg,#5a6270 0%,var(--steel) 40%,var(--navy) 100%)"></div>
  <div class="brand brand--left" style="top:42px;color:var(--navy)">
    <span class="brand__mark"></span>
    <span class="brand__name">Velmora<br>Asset Management</span>
  </div>
  <h1 class="title align-left" style="top:218px;color:var(--navy)">Your Title Goes Here</h1>
  <p class="subtitle align-left" style="top:262px;color:var(--navy)">Your subtitle goes here</p>
  <span class="rule" style="left:0;width:400px;top:426px;background:#c9ccd6"></span>
  <span class="site" style="left:408px;top:419px;color:#9a9fb2">www.velmoraam.com</span>
</section>

<!-- Cover 4 : dark, left aligned -->
<section class="slide slide--4 dark">
  <div class="fill" role="img" aria-label="Navy tinted photograph of a modern building facade"
       style="inset:0;background:linear-gradient(135deg,#2c3478 0%,var(--navy) 45%,#323a80 75%,#2a3176 100%)"></div>
  <div class="fill" role="img" aria-label="Abstract geometric decoration with monochrome building photograph"
       style="right:0;top:0;width:290px;height:472px;clip-path:polygon(100% 0,100% 100%,10% 100%,35% 55%);background:linear-gradient(200deg,#e6e8ec 0%,#8a8f99 45%,#3a3d46 100%)"></div>
  <div class="brand brand--left" style="top:42px">
    <span class="brand__mark"></span>
    <span class="brand__name">Velmora<br>Asset Management</span>
  </div>
  <h1 class="title align-left" style="top:216px">Your Title Goes Here</h1>
  <p class="subtitle align-left" style="top:260px">Your subtitle goes here</p>
  <span class="rule" style="left:0;width:180px;top:426px"></span>
  <span class="site" style="left:386px;top:419px">www.velmoraam.com</span>
</section>

<!-- Divider 1 -->
<section class="slide slide--5 dark">
  <div class="fill" style="inset:0;background:var(--navy)"></div>
  <div class="fill" style="left:0;top:0;width:590px;height:472px;clip-path:polygon(0 0,100% 0,52% 100%,0 100%);background:#8c919c"></div>
  <div class="fill" role="img" aria-label="Upward view of glass skyscraper facade against the sky"
       style="left:0;top:0;width:570px;height:472px;clip-path:polygon(0 0,100% 0,49% 100%,0 100%);background:linear-gradient(135deg,#1a1c22 0%,#6d7380 35%,#dfe3ea 60%,#9aa1ad 100%)"></div>
  <div class="brand brand--right" style="top:64px">
    <span class="brand__mark" style="width:24px;height:24px"></span>
    <span class="brand__name" style="font-size:15px">Velmora<br>Asset Management</span>
  </div>
  <h2 class="divider-title">This is your<br>divider page</h2>
  <p class="subtitle divider-sub">Your subtitle goes here</p>
</section>

<!-- Divider 2 -->
<section class="slide slide--6" style="background:var(--paper)">
  <div class="fill" role="img" aria-label="Navy tinted photograph of glass office towers"
       style="left:0;top:0;width:100%;height:266px;background:linear-gradient(180deg,#3d4584 0%,#353d7e 50%,#2c3476 100%)"></div>
  <div class="banner-band"></div>
  <div class="brand brand--left" style="top:322px;color:var(--navy)">
    <span class="brand__mark" style="width:26px;height:26px"></span>
    <span class="brand__name" style="font-size:17px">Velmora<br>Asset Management</span>
  </div>
  <h2 class="banner-title">This is your divider page</h2>
</section>

</body>
</html>
```